New Business Card Design for Manufacturing

We are an engineering/manufacturing company that offers Advanced machining/assembly/engineering services, as well as innovative products for the heavy duty engine cooling markets.

We are looking to get a new business card designed that is clean and modern looking, but still fits the wide range of technical/skilled work we do.

- We hope to use this design as the base for other design work in new Presentations, web, and print work.

Industry/Entity Type

Engineering

Contact Information for Business Card

Our preferred color of blue is (RGB) 22/71/159 but can vary slightly from that color. Our content will be our Logo and full company name (Fabricated Tooling Works, Inc.), company address, name, job title, phone number with extension, cell number, fax number, website, and email address on the cards.
We'd like the full company name next to the logo, but we are open to other interpretations of that layout.
Preferably, we would like the back side to be clean with just our logo, and the front to contain all of the contact information.

Colors
2f74b4
0355a3
85abd2

Requirements
Must have
• - Logo, company name, needed content - We are open to interpretation beyond that.
• - Standard size business card.
• - Horizontal orientation.
• - Enough space for lengthy names / job titles (for example, a job title could read "Directory of Human Resources" or "V.P. of Governmental Affairs"). We need this to look clean, whether the title be short (CEO) or long (as described above).

```html
<!DOCTYPE html>
<html lang="en">
<head>
<meta charset="utf-8">
<title>Fabricated Tooling Works – Business Card</title>
<link href="https://fonts.googleapis.com/css2?family=Open+Sans:wght@400;600;800&family=Crimson+Text:wght@400&display=swap" rel="stylesheet">
<style>
  :root {
    --brand-blue: #16479f;
    --mid-blue: #0355a3;
    --light-blue: #85abd2;
    --grey-band: #7d8387;
    --ink: #3a3f45;
    --paper: #ffffff;
    --stage: #eceef0;
  }
  * { box-sizing: border-box; margin: 0; padding: 0; }
  html, body { width: 1200px; height: 1200px; overflow: hidden; }
  body {
    background: var(--stage);
    font-family: "Open Sans", Arial, sans-serif;
    position: relative;
  }
  .card {
    position: absolute;
    left: 240px;
    width: 720px;
    height: 412px;
    overflow: hidden;
    box-shadow: 0 10px 28px rgba(0,0,0,.18);
  }
  /* Back side */
  .card-back {
    top: 110px;
    background: radial-gradient(ellipse at 50% 40%, #1f5fb5 0%, var(--brand-blue) 40%, #0c2f6b 100%);
    display: flex;
    align-items: center;
    justify-content: center;
  }
  .wordmark { display: flex; align-items: center; gap: 14px; }
  .wordmark-square { width: 30px; height: 30px; background: currentColor; flex: none; }
  .wordmark-name {
    font-weight: 800;
    font-size: 30px;
    letter-spacing: .5px;
    text-transform: uppercase;
    line-height: 1.08;
  }
  .card-back .wordmark { color: var(--paper); }

  /* Front side */
  .card-front { top: 660px; background: var(--paper); }
  .front-logo { position: absolute; left: 44px; top: 66px; color: var(--brand-blue); }
  .front-logo .wordmark-name { font-size: 26px; }
  .front-logo .wordmark-square { width: 24px; height: 24px; }
  .company-full {
    position: absolute;
    left: 44px; top: 160px;
    font-size: 14px;
    color: var(--ink);
  }
  .person-name {
    position: absolute;
    right: 40px; top: 36px;
    font-family: "Crimson Text", Georgia, serif;
    font-size: 30px;
    line-height: 1;
    color: var(--brand-blue);
  }
  .rule-top {
    position: absolute;
    left: 340px; right: 40px; top: 76px;
    height: 1px; background: var(--brand-blue);
  }
  .person-title {
    position: absolute;
    right: 40px; top: 84px;
    font-size: 13px;
    color: var(--ink);
  }
  .rule-contact {
    position: absolute;
    left: 44px; width: 420px; top: 196px;
    height: 1px; background: var(--brand-blue);
  }
  .contact-list {
    position: absolute;
    left: 44px; top: 206px;
    list-style: none;
    font-size: 16px;
    color: var(--ink);
  }
  .contact-list li { display: flex; align-items: center; gap: 10px; height: 24px; }
  .contact-list .ext { color: var(--brand-blue); }
  .contact-icon { width: 16px; height: 16px; flex: none; }
  .footer-bands { position: absolute; left: 0; bottom: 0; width: 720px; height: 120px; }
  .address {
    position: absolute;
    left: 44px; bottom: 26px;
    color: var(--paper);
    font-size: 17px;
    line-height: 1.2;
  }
  .website {
    position: absolute;
    right: 22px; top: 312px;
    color: var(--paper);
    font-size: 13px;
    line-height: 1.2;
  }
</style>
</head>
<body>

<section class="card card-back" aria-label="Card back">
  <div class="wordmark">
    <span class="wordmark-square"></span>
    <span class="wordmark-name">Fabricated<br>Tooling Works</span>
  </div>
</section>

<section class="card card-front" aria-label="Card front">
  <div class="front-logo wordmark">
    <span class="wordmark-square"></span>
    <span class="wordmark-name">Fabricated<br>Tooling Works</span>
  </div>
  <p class="company-full">Fabricated Tooling Works, Inc.</p>

  <p class="person-name">Daniel Mercer</p>
  <div class="rule-top"></div>
  <p class="person-title">Director</p>

  <div class="rule-contact"></div>
  <ul class="contact-list">
    <li>
      <svg class="contact-icon" viewBox="0 0 16 16" aria-hidden="true"><rect width="16" height="16" rx="3" fill="#16479f"/><path d="M4 5c0-1 1-1.5 2-1l1 2-1 1c.5 1.2 1.5 2.2 2.8 2.8l1-1 2 1c.5 1 0 2-1 2C7 11.8 4.2 9 4 5z" fill="#fff"/></svg>
      <span>1 - 555 201 4480 <span class="ext">(EXT)</span></span>
    </li>
    <li>
      <svg class="contact-icon" viewBox="0 0 16 16" aria-hidden="true"><rect width="16" height="16" rx="3" fill="#16479f"/><rect x="3.5" y="6" width="9" height="6" rx="1" fill="#fff"/><rect x="5" y="3.5" width="6" height="3" fill="#fff"/></svg>
      <span>1 - 555 201 4485</span>
    </li>
    <li>
      <svg class="contact-icon" viewBox="0 0 16 16" aria-hidden="true"><rect width="16" height="16" rx="3" fill="#16479f"/><rect x="5.5" y="3" width="5" height="10" rx="1" fill="#fff"/></svg>
      <span>1 - 555 309 7712</span>
    </li>
    <li>
      <svg class="contact-icon" viewBox="0 0 16 16" aria-hidden="true"><rect width="16" height="16" rx="3" fill="#16479f"/><rect x="3" y="5" width="10" height="7" fill="#fff"/><path d="M3 5l5 4 5-4" stroke="#16479f" fill="none"/></svg>
      <span>daniel@ftworks.com</span>
    </li>
  </ul>

  <svg class="footer-bands" viewBox="0 0 720 120" aria-hidden="true">
    <polygon points="450,0 720,0 720,120 510,120" fill="#7d8387"/>
    <polygon points="0,40 420,40 460,120 0,120" fill="#16479f"/>
  </svg>
  <p class="address">Harbor City, Westland</p>
  <p class="website">www.fabricatedtoolingworks.com</p>
</section>

</body>
</html>
```